Political Mail Out Quintero front and back

Front
Esteban (Hall Pass) Quintero!

What's that famous saying?

Show me who your friends are and I'll tell you who you really are!
(show the two guys)

Arturo Benavides is charged with voter fraud by changing voter addresses from across the RGV so they could vote in Edinburg
Back
Did Esteban (Hall Pass) Quintero commit voter fraud when he ran for office in 2016?
(insert blurred photo)

Here is a list of people from all over the RGV that voted in Edinburg in the 2016 race.
Here is a break down:

(highlight the number and where they were first registered to vote)

9 People voted in Edinburg who were registered in Donna.
13 People voted in Edinburg who were registered in San Juan
8 People voted in Edinburg who were registered in Pharr
31 People voted in Edinburg who were registered in McAllen
2 People voted in Edinburg who were registered in La Joya
6 People voted in Edinburg who were registered in Edcouch
2 People voted in Edinburg who were registered in Mercedes
2 People voted in Edinburg who were registered in Monte Alto
6 People voted in Edinburg who were registered in Weslaco
1 Person voted in Edinburg who were registered in Penitas
3 People voted in Edinburg who were registered in Alamo
5 People voted in Edinburg who were registered in Elsa
6 People voted in Edinburg who were registered in Mission
1 Person voted in Edinburg who were registered in Alton

Will Esteban (Hall Pass) Quintero CHEAT in 2020?

Only time will tell.

Vote Esteban (Hall Pass) Quintero OUT of office.

```html
<!DOCTYPE html>
<html lang="en">
<head>
<meta charset="utf-8">
<title>Political Mail Out – Quintero – Front and Back</title>
<link rel="stylesheet" href="https://fonts.googleapis.com/css2?family=Montserrat:wght@300;400;500;700;800&display=swap">
<style>
  :root {
    --backdrop: #b3b3b3;
    --navy: #1e2a5a;
    --navy-deep: #182149;
    --red: #d42326;
    --red-deep: #a91b1e;
    --white: #ffffff;
    --stamp: #e6e6e6;
    --rule: #cfcfcf;
    --photo-warm: #b59a86;
    --photo-cool: #8a8f96;
  }
  * { box-sizing: border-box; margin: 0; padding: 0; }
  html, body {
    width: 800px; height: 1200px; overflow: hidden;
    background: var(--backdrop);
    font-family: "Montserrat", Arial, sans-serif;
  }
  .canvas { position: relative; width: 800px; height: 1200px; }

  .postcard {
    position: absolute; left: 30px; width: 740px; height: 529px;
    overflow: hidden; box-shadow: 0 1px 3px rgba(0,0,0,.25);
  }
  .postcard--front { top: 50px; background: linear-gradient(var(--navy) 0 287px, var(--red) 287px); }
  .postcard--back { top: 620px; background: var(--white); }

  .star-rule { position: absolute; left: 0; height: 3px; background: var(--white); }
  .star-row { position: absolute; display: flex; color: var(--white); font-size: 16px; line-height: 1; }

  /* FRONT */
  .vote-mark {
    position: absolute; left: 30px; top: 38px;
    font-weight: 800; font-size: 92px; letter-spacing: 1px; color: var(--white); line-height: 1;
  }
  .vote-mark .tick { position: absolute; left: 78px; top: -10px; width: 70px; height: 70px; }
  .candidate { position: absolute; left: 30px; top: 146px; color: var(--white); line-height: 1.02; }
  .candidate__first { font-weight: 700; font-size: 31px; letter-spacing: .5px; }
  .candidate__nick { font-weight: 300; font-size: 31px; letter-spacing: .5px; }
  .candidate__last { font-weight: 800; font-size: 44px; letter-spacing: .5px; }

  .message { position: absolute; left: 33px; top: 315px; width: 300px; color: var(--white); }
  .message__title { font-weight: 700; font-size: 20px; margin-bottom: 16px; }
  .message__saying { font-weight: 700; font-size: 14.5px; line-height: 1.25; margin-bottom: 18px; }
  .message__charge { font-weight: 400; font-size: 14.5px; line-height: 1.25; }
  .message__charge strong { font-weight: 700; }

  .photo-frame {
    position: absolute; left: 360px; top: 26px; width: 359px; height: 473px;
    background: linear-gradient(var(--navy-deep) 0 261px, var(--red-deep) 261px);
  }
  .photo-frame__photo {
    position: absolute; left: 15px; top: 17px; width: 330px; height: 438px;
    border: 2px solid var(--white);
    background: linear-gradient(160deg, #6f6a66 0%, var(--photo-warm) 40%, #d9d6d2 60%, var(--photo-cool) 100%);
  }

  /* BACK */
  .back__panel {
    position: absolute; left: 0; top: 0; width: 408px; height: 529px;
    background: linear-gradient(var(--navy) 0 434px, var(--red) 434px);
  }
  .back__edge { position: absolute; left: 408px; top: 0; width: 4px; height: 529px; background: var(--white); }
  .back__edge-red { position: absolute; left: 412px; top: 0; width: 6px; height: 529px; background: var(--red); }

  .intro { position: absolute; left: 29px; top: 24px; width: 255px; color: var(--white); font-size: 9.4px; line-height: 1.3; }
  .intro p { margin-bottom: 7px; }
  .portrait {
    position: absolute; left: 296px; top: 22px; width: 97px; height: 73px;
    border: 2px solid var(--white); outline: 2px solid var(--red);
    background: radial-gradient(circle at 50% 45%, #d8c4b4 0 22%, #eeeeee 40%, #f6f6f6 100%);
  }
  .tally { position: absolute; top: 118px; width: 166px; list-style: none; color: var(--white); font-size: 9.2px; line-height: 12.3px; }
  .tally--left { left: 31px; }
  .tally--right { left: 217px; }
  .tally li { position: relative; padding-left: 14px; margin-bottom: 13.5px; }
  .tally li svg { position: absolute; left: 0; top: 2px; width: 9px; height: 9px; }
  .tally .count { color: var(--red); font-weight: 700; }

  .closing { position: absolute; left: 27px; top: 453px; color: var(--white); font-weight: 700; font-size: 10.6px; line-height: 17.5px; }
  .evidence {
    position: absolute; left: 348px; top: 412px; width: 44px; height: 92px;
    border: 1px solid var(--white);
    background: linear-gradient(90deg, #9a9a9a, #d8d8d8 40%, #b5b5b5 70%, #8c8c8c);
  }

  .stamp { position: absolute; left: 631px; top: 64px; width: 82px; height: 79px; background: var(--stamp); }
  .address-line { position: absolute; left: 464px; width: 248px; height: 1px; background: var(--rule); }
</style>
</head>
<body>
<main class="canvas">

  <section class="postcard postcard--front" aria-label="Mail out front">
    <div class="vote-mark">VOTE
      <svg class="tick" viewBox="0 0 70 70" aria-hidden="true">
        <path d="M14 38 L30 56 L66 4 L58 2 L30 44 L20 32 Z" fill="#d42326"/>
      </svg>
    </div>
    <h1 class="candidate">
      <span class="candidate__first">ESTEBAN</span><br>
      <span class="candidate__nick">(HALL PASS)</span><br>
      <span class="candidate__last">QUINTERO!</span>
    </h1>

    <div class="star-rule" style="top:286px;width:360px"></div>
    <div class="star-row" style="left:33px;top:279px;gap:32px">
      <span>★</span><span>★</span><span>★</span><span>★</span><span>★</span>
    </div>

    <div class="message">
      <p class="message__title">What's that famous saying?</p>
      <p class="message__saying">Show me who your friends are and I'll tell you who you really are!</p>
      <p class="message__charge"><strong>Arturo Benavides is charged with voter fraud by</strong> changing voter addresses from across the RGV so they could vote in Edinburg</p>
    </div>

    <div class="photo-frame">
      <div class="photo-frame__photo" role="img" aria-label="Photo of Esteban Quintero and Arturo Benavides standing together, smiling"></div>
    </div>
  </section>

  <section class="postcard postcard--back" aria-label="Mail out back">
    <div class="back__panel">
      <div class="intro">
        <p>Did Esteban (Hall Pass) Quintero commit voter fraud when he ran for office in 2016?</p>
        <p>Here is a list of people from all over the RGV that voted in Edinburg in the 2016 race.</p>
        <p>Here is a break down:</p>
      </div>
      <div class="portrait" role="img" aria-label="Blurred photo of a man"></div>

      <ul class="tally tally--left">
        <li><svg viewBox="0 0 9 9"><rect width="9" height="9" fill="#fff"/><path d="M1.5 4.5 L3.8 7 L8 1" stroke="#d42326" stroke-width="1.8" fill="none"/></svg><span class="count">9</span> People voted in Edinburg who were registered in Donna.</li>
        <li><svg viewBox="0 0 9 9"><rect width="9" height="9" fill="#fff"/><path d="M1.5 4.5 L3.8 7 L8 1" stroke="#d42326" stroke-width="1.8" fill="none"/></svg><span class="count">13</span> People voted in Edinburg who were registered in San Juan</li>
        <li><svg viewBox="0 0 9 9"><rect width="9" height="9" fill="#fff"/><path d="M1.5 4.5 L3.8 7 L8 1" stroke="#d42326" stroke-width="1.8" fill="none"/></svg><span class="count">8</span> People voted in Edinburg who were registered in Pharr</li>
        <li><svg viewBox="0 0 9 9"><rect width="9" height="9" fill="#fff"/><path d="M1.5 4.5 L3.8 7 L8 1" stroke="#d42326" stroke-width="1.8" fill="none"/></svg><span class="count">31</span> People voted in Edinburg who were registered in McAllen</li>
        <li><svg viewBox="0 0 9 9"><rect width="9" height="9" fill="#fff"/><path d="M1.5 4.5 L3.8 7 L8 1" stroke="#d42326" stroke-width="1.8" fill="none"/></svg><span class="count">2</span> People voted in Edinburg who were registered in La Joya</li>
        <li><svg viewBox="0 0 9 9"><rect width="9" height="9" fill="#fff"/><path d="M1.5 4.5 L3.8 7 L8 1" stroke="#d42326" stroke-width="1.8" fill="none"/></svg><span class="count">6</span> People voted in Edinburg who were registered in Edcouch</li>
        <li><svg viewBox="0 0 9 9"><rect width="9" height="9" fill="#fff"/><path d="M1.5 4.5 L3.8 7 L8 1" stroke="#d42326" stroke-width="1.8" fill="none"/></svg><span class="count">2</span> People voted in Edinburg who were registered in Mercedes</li>
      </ul>
      <ul class="tally tally--right">
        <li><svg viewBox="0 0 9 9"><rect width="9" height="9" fill="#fff"/><path d="M1.5 4.5 L3.8 7 L8 1" stroke="#d42326" stroke-width="1.8" fill="none"/></svg><span class="count">2</span> People voted in Edinburg who were registered in Monte Alto</li>
        <li><svg viewBox="0 0 9 9"><rect width="9" height="9" fill="#fff"/><path d="M1.5 4.5 L3.8 7 L8 1" stroke="#d42326" stroke-width="1.8" fill="none"/></svg><span class="count">6</span> People voted in Edinburg who were registered in Weslaco</li>
        <li><svg viewBox="0 0 9 9"><rect width="9" height="9" fill="#fff"/><path d="M1.5 4.5 L3.8 7 L8 1" stroke="#d42326" stroke-width="1.8" fill="none"/></svg><span class="count">1</span> Person voted in Edinburg who were registered in Penitas</li>
        <li><svg viewBox="0 0 9 9"><rect width="9" height="9" fill="#fff"/><path d="M1.5 4.5 L3.8 7 L8 1" stroke="#d42326" stroke-width="1.8" fill="none"/></svg><span class="count">3</span> People voted in Edinburg who were registered in Alamo</li>
        <li><svg viewBox="0 0 9 9"><rect width="9" height="9" fill="#fff"/><path d="M1.5 4.5 L3.8 7 L8 1" stroke="#d42326" stroke-width="1.8" fill="none"/></svg><span class="count">5</span> People voted in Edinburg who were registered in Elsa</li>
        <li><svg viewBox="0 0 9 9"><rect width="9" height="9" fill="#fff"/><path d="M1.5 4.5 L3.8 7 L8 1" stroke="#d42326" stroke-width="1.8" fill="none"/></svg><span class="count">6</span> People voted in Edinburg who were registered in Mission</li>
        <li><svg viewBox="0 0 9 9"><rect width="9" height="9" fill="#fff"/><path d="M1.5 4.5 L3.8 7 L8 1" stroke="#d42326" stroke-width="1.8" fill="none"/></svg><span class="count">1</span> Person voted in Edinburg who were registered in Alton</li>
      </ul>

      <div class="star-rule" style="top:433px;width:408px"></div>
      <div class="star-row" style="left:30px;top:426px;gap:32px">
        <span>★</span><span>★</span><span>★</span><span>★</span><span>★</span><span>★</span><span>★</span>
      </div>

      <p class="closing">Will Esteban (Hall Pass) Quintero CHEAT in 2020?<br>Only time will tell.<br>Vote Esteban (Hall Pass) Quintero OUT of office.</p>
      <div class="evidence" role="img" aria-label="Photo of a printed voter record"></div>
    </div>
    <div class="back__edge"></div>
    <div class="back__edge-red"></div>

    <div class="stamp" aria-label="Stamp area"></div>
    <div class="address-line" style="top:202px"></div>
    <div class="address-line" style="top:241px"></div>
    <div class="address-line" style="top:280px"></div>
    <div class="address-line" style="top:320px"></div>
    <div class="address-line" style="top:360px"></div>
  </section>

</main>
</body>
</html>
```